Website Design for recruiting company

We need a homepage mockup for a recruiting company focused on the legal industry. Use your creative talent to come up with something visually appeal and professional for this web-site.

We'd really like to see the maze from the logo incorporated into the design somehow. Please use the website mockup provided as inspiration for this project. We really like the layout and photos!

Target Market(s)

lawyers

Industry/Entity Type

Legal

Number of Pages Required

1 page

Font styles to use
Sans Serif

```html
<!DOCTYPE html>
<html lang="en">
<head>
<meta charset="utf-8">
<title>Harborline Legal Search</title>
<link href="https://fonts.googleapis.com/css2?family=Cabin:wght@400;500;600&family=Oswald:wght@600&family=Arimo:wght@400&display=swap" rel="stylesheet">
<style>
:root{
  --sage:#a9b59f;
  --plum:#766775;
  --plum-dark:#6e5f6d;
  --heading:#7a6979;
  --panel:#e4e1e4;
  --mist:#e9ebe6;
  --ink:#4a4a4a;
  --white:#ffffff;
}
*{margin:0;padding:0;box-sizing:border-box}
html,body{width:1200px;height:3177px;overflow:hidden}
body{position:relative;background:var(--white);font-family:"Arimo",Arial,sans-serif;color:var(--ink)}
.abs{position:absolute}
.btn{position:absolute;display:flex;align-items:center;justify-content:center;background:var(--sage);color:var(--white);border-radius:26px;font-family:"Cabin",sans-serif;font-size:18px;letter-spacing:.3px;text-transform:uppercase}
.photo{position:absolute}

/* header / hero */
.hero{left:0;top:0;width:1200px;height:676px;background:linear-gradient(110deg,#5b4a45 0%,#7a6a62 30%,#4d4f55 60%,#2e3138 100%)}
.brand{position:absolute;display:flex;align-items:center;gap:10px;font-family:"Cabin",sans-serif;font-size:13px;color:var(--white)}
.brand-mark{width:72px;height:72px;border-radius:50%;border:3px solid #e8e8e8}
.nav{left:578px;top:27px;display:flex;align-items:center;gap:0;font-family:"Arimo",sans-serif;font-size:15px;color:#f2f2f2}
.nav a{color:inherit;text-decoration:none;padding:0 12px;height:41px;display:flex;align-items:center}
.nav a.active{background:var(--sage);border-radius:21px;padding:0 20px;margin-right:10px}
.hero-title{right:92px;top:264px;text-align:right;font-family:"Oswald",sans-serif;font-weight:600;font-size:50px;letter-spacing:-.6px;line-height:60px;color:var(--white);text-transform:uppercase}
.dots{left:1153px;top:326px;display:flex;flex-direction:column;gap:9px}
.dots span{width:12px;height:12px;border:1.5px solid #fff;border-radius:50%}
.dots span.on{width:14px;height:14px;margin-left:-1px;background:radial-gradient(circle,#fff 35%,transparent 40%)}

/* search band */
.finder{left:0;top:676px;width:1200px;height:104px;background:var(--plum)}
.finder h2{position:absolute;left:110px;top:32px;font-family:"Cabin",sans-serif;font-weight:500;font-size:32px;color:var(--white)}
.field{position:absolute;background:var(--white);border-radius:24px;font-size:14px;color:#9a9a9a;display:flex;align-items:center;padding-left:20px}

/* split sections */
h3.section-title{font-family:"Cabin",sans-serif;font-weight:500;font-size:42px;color:var(--heading)}
.copy{font-size:15.5px;line-height:27px;color:#555}
.ring{position:absolute;border-radius:50%;background:var(--plum)}

/* listings */
.listings{left:0;top:1301px;width:1200px;height:619px;background:var(--mist)}
.card{position:absolute;top:1499px;width:246px;height:280px;background:var(--white)}
.card .photo{left:9px;top:8px;width:229px;height:166px}
.card h4{position:absolute;left:15px;top:195px;font-family:"Cabin",sans-serif;font-weight:500;font-size:21px;color:var(--heading)}
.card p{position:absolute;left:15px;top:225px;font-size:15.5px;letter-spacing:.3px;color:#555}

/* banner */
.banner{left:0;top:2441px;width:1200px;height:375px;background:linear-gradient(90deg,#6a5e58 0%,#8a7a70 25%,#6c6068 50%,#5d5460 100%)}

/* footer */
.footer{left:0;top:2816px;width:1200px;height:361px;background:var(--plum);color:#f1eef1}
.footer h5{position:absolute;top:44px;font-family:"Cabin",sans-serif;font-weight:500;font-size:18px}
.footer ul{position:absolute;top:82px;list-style:none;font-size:15.5px;letter-spacing:.3px}
.footer li{height:31px;position:relative;padding-left:14px}
.footer li::before{content:"";position:absolute;left:0;top:8px;width:4px;height:4px;border-radius:50%;background:#f1eef1}
.contact{position:absolute;left:877px;display:flex;align-items:center;gap:12px;font-family:"Cabin",sans-serif;font-size:16px}
.legal{position:absolute;left:0;width:1200px;top:318px;text-align:center;font-family:"Cabin",sans-serif;font-size:14px}
</style>
</head>
<body>

<!-- Hero -->
<section class="abs hero" role="img" aria-label="Photo of a smiling woman shaking hands across a desk in a bright office"></section>
<div class="brand" style="left:76px;top:12px"><span class="brand-mark"></span>harborline legal search</div>
<nav class="abs nav">
  <a class="active" href="#">Home</a><a href="#">About Us</a><a href="#">Whats's New</a><a href="#">For Employers</a><a href="#">Contact Us</a>
  <svg width="20" height="20" viewBox="0 0 20 20" style="margin-left:10px"><circle cx="8" cy="8" r="6" fill="none" stroke="#fff" stroke-width="2.5"/><line x1="12.5" y1="12.5" x2="18" y2="18" stroke="#fff" stroke-width="3" stroke-linecap="round"/></svg>
</nav>
<h1 class="abs hero-title">Start here,<br>let our experience<br>guide you</h1>
<div class="btn" style="left:938px;top:462px;width:166px;height:51px">Search Job</div>
<div class="abs dots"><span></span><span></span><span class="on"></span><span></span><span></span></div>

<!-- Job finder -->
<section class="abs finder">
  <h2>Find Your Perfect Job.</h2>
  <div class="field" style="left:423px;top:31px;width:249px;height:45px">Job Title or Keyword</div>
  <div class="field" style="left:680px;top:31px;width:249px;height:45px">City, State , Zip</div>
  <div class="btn" style="left:937px;top:31px;width:156px;height:45px">Search Job</div>
</section>

<!-- About -->
<div class="abs" style="left:0;top:780px;width:364px;height:521px;background:var(--panel)"></div>
<div class="ring" style="left:181px;top:860px;width:366px;height:370px"></div>
<div class="photo" style="left:185px;top:858px;width:358px;height:358px;border-radius:50%;background:linear-gradient(135deg,#c9c7c2,#8f7f70 45%,#3d4656)" role="img" aria-label="Photo of business people shaking hands in an office corridor"></div>
<h3 class="abs section-title" style="left:617px;top:884px">About Us</h3>
<p class="abs copy" style="left:617px;top:950px;width:440px">Harborline Legal Search focuses on the permanent placement of attorneys with law firms and corporations in the New England area. Founded in 1982, Harborline Legal Search is the oldest attorney search firm in New England, and is ranked the number one legal recruiter in New England in the most recent survey conducted by The Counsel Review</p>
<div class="btn" style="left:617px;top:1127px;width:165px;height:51px">Learn More</div>

<!-- What's New -->
<section class="abs listings"></section>
<h3 class="abs section-title" style="left:0;top:1360px;width:1200px;text-align:center">Whats's New</h3>
<p class="abs copy" style="left:350px;top:1421px;width:500px;text-align:center;line-height:25px">Below are our most recent listings. All positions are in the greater Boston area unless otherwise noted.</p>
<article class="card" style="left:76px"><div class="photo" style="background:linear-gradient(180deg,#d8d0c4,#3f4c78 70%,#b88a6a)" role="img" aria-label="Photo of a modern office lounge with people working"></div><h4>Job Title</h4><p>Harborline legal Search</p></article>
<article class="card" style="left:344px"><div class="photo" style="background:linear-gradient(180deg,#cfd3d6,#9a8c78 55%,#5f6a4a)" role="img" aria-label="Photo of a glass-walled office with plants"></div><h4>Job Title</h4><p>Harborline legal Search</p></article>
<article class="card" style="left:610px"><div class="photo" style="background:linear-gradient(180deg,#9b6a55,#c9b7a8 60%,#e6e2dc)" role="img" aria-label="Photo of colleagues at desks in a brick-walled office"></div><h4>Job Title</h4><p>Harborline legal Search</p></article>
<article class="card" style="left:877px"><div class="photo" style="background:linear-gradient(135deg,#3d4a5e,#dcd9d4 50%,#8a8078)" role="img" aria-label="Photo of a team meeting in a creative office"></div><h4>Job Title</h4><p>Harborline legal Search</p></article>
<div class="btn" style="left:485px;top:1809px;width:165px;height:51px">Search Job</div>

<!-- For Employers -->
<div class="abs" style="left:836px;top:1920px;width:364px;height:521px;background:var(--panel)"></div>
<div class="ring" style="left:653px;top:2002px;width:366px;height:366px"></div>
<div class="photo" style="left:655px;top:1998px;width:362px;height:360px;border-radius:50%;background:linear-gradient(180deg,#e6e6e4,#cfcdca 55%,#b9b2a6)" role="img" aria-label="Photo of job candidates waiting on chairs for interviews"></div>
<h3 class="abs section-title" style="left:125px;top:2076px">For Employers</h3>
<p class="abs copy" style="left:125px;top:2141px;width:425px">Our unparalleled recruiting industry and legal experience have generated an extensive network of contacts throughout the legal community.</p>
<div class="field" style="left:118px;top:2246px;width:484px;height:50px;border:1px solid #ddd;border-radius:26px">Find The Right Candidate</div>
<div class="btn" style="left:437px;top:2246px;width:165px;height:50px">Start Here</div>

<!-- Talent banner -->
<section class="abs banner" role="img" aria-label="Photo of a smiling businessman on a phone call holding a coffee cup"></section>
<h3 class="abs" style="left:667px;top:2548px;font-family:'Cabin',sans-serif;font-weight:500;font-size:39px;line-height:45px;color:#fff">Delivering the Talent<br>Your Business Needs.</h3>
<p class="abs" style="left:671px;top:2652px;font-size:17px;letter-spacing:.5px;color:#fff">Harborline legal Search</p>
<div class="btn" style="left:667px;top:2689px;width:207px;height:51px">Request Talent</div>

<!-- Footer -->
<footer class="abs footer">
  <h5 style="left:81px">Sitemap</h5>
  <ul style="left:81px"><li>Home</li><li>About Us</li><li>Whats's New</li><li>For Employers</li><li>Contact Us</li></ul>
  <h5 style="left:347px">Quick Links</h5>
  <ul style="left:347px"><li>Help</li><li>Serach Job</li><li>Hire Talent</li><li>Tearm &amp;</li><li>Condition</li><li>Privacy Policy</li></ul>
  <h5 style="left:612px">Follow Us</h5>
  <ul style="left:612px"><li>Newsfeed</li><li>Pro Network</li><li>Microblog</li><li>Photo Feed</li></ul>
  <div class="brand" style="left:877px;top:36px"><span class="brand-mark"></span>harborline legal search</div>
  <div class="contact" style="top:134px"><svg width="20" height="20" viewBox="0 0 24 24"><path d="M6.6 10.8a15 15 0 0 0 6.6 6.6l2.2-2.2a1 1 0 0 1 1-.25 11.4 11.4 0 0 0 3.6.57 1 1 0 0 1 1 1V20a1 1 0 0 1-1 1A17 17 0 0 1 3 4a1 1 0 0 1 1-1h3.5a1 1 0 0 1 1 1c0 1.25.2 2.45.57 3.57a1 1 0 0 1-.25 1z" fill="#f1eef1"/></svg>555 010 2244</div>
  <div class="contact" style="top:174px"><svg width="20" height="16" viewBox="0 0 20 16"><rect x="0" y="0" width="20" height="16" rx="2" fill="#f1eef1"/><path d="M1 2l9 7 9-7" fill="none" stroke="#766775" stroke-width="1.8"/></svg>info@harborlinelegal.com</div>
  <p class="legal">©NORTHGATE STUDIO -2020 All rights reserved.</p>
</footer>

</body>
</html>
```